Leadership and Team Coaching Blog Template for my company, Garnet Lowell Pty Ltd

I need a consistent design I can use for publications. I am a leadership coach as well as a team coach and I also am a pretty good facilitator. I am to help people be their best both as individuals and as teams so as I enter semi-retirement I've been writing short articles to support my business. The final design should be flexible and elegant so you can tell the difference between different articles. It should also communicate confidence, energy and expertise and invite you to read further. I love blue and have attached my current logo. Not wedded to using it but clients recognise it and am sure someone clever can do something interesting with it

Target Market(s)

middle and senior leaders and Board members

Industry/Entity Type

It Company

Font styles to use
Sans Serif

Colors
0392cd
3176b5
3276b5
886aae
33b8a4
00a990
a54499
c588bc
876aae

Requirements
Must have
• flexibility to be able to re-use for different publications
Nice to have
• eye catching images
• elegant line drawing
Should not have
• clip art

```html
<!DOCTYPE html>
<html lang="en">
<head>
<meta charset="utf-8">
<title>Garnet Lowell Pty Ltd — Leadership &amp; Team Coaching</title>
<link href="https://fonts.googleapis.com/css2?family=Jost:wght@400;500;600;700&display=swap" rel="stylesheet">
<style>
:root{
  --blue:#0392cd;
  --blue-deep:#3176b5;
  --violet:#886aae;
  --plum:#a54499;
  --orchid:#b56fb0;
  --teal:#33b8a4;
  --green:#00a990;
  --ink:#222;
  --muted:#8a8a8a;
  --body:#9a9a9a;
  --paper:#fff;
  --mist:#f4f4f4;
  --fog:#ececec;
  --footer:#2f6fb0;
}
*{margin:0;padding:0;box-sizing:border-box}
html,body{width:1200px;height:3390px;overflow:hidden}
body{font-family:"Jost",sans-serif;color:var(--ink);background:var(--paper);position:relative}
.abs{position:absolute}

/* header */
.site-header{left:0;top:0;width:1200px;height:120px;background:var(--paper)}
.brand{left:100px;top:30px;display:flex;align-items:center;gap:12px}
.brand-mark{width:14px;height:14px;background:var(--blue-deep)}
.brand-name{font-size:22px;font-weight:500;color:var(--blue-deep);letter-spacing:1px;line-height:1.1}
.main-nav{right:100px;top:50px;display:flex;gap:50px;font-size:14px;letter-spacing:.5px;color:#333}
.main-nav .active{color:var(--blue)}

/* hero */
.hero{left:0;top:120px;width:1200px;height:547px;
  background:radial-gradient(ellipse 380px 220px at 660px 170px,#c98a3a 0%,#8a5a2a 35%,#3a2a1c 70%,#141210 100%)}
.hero-title{left:0;width:1200px;top:190px;text-align:center;color:#fff;font-size:36px;font-weight:600;letter-spacing:.5px}
.hero-sub{left:0;width:1200px;top:242px;text-align:center;color:#eee;font-size:19px}
.hero-arrow{top:212px;width:46px;height:46px;border-radius:50%;background:rgba(255,255,255,.25)}

/* articles */
.articles{left:0;top:667px;width:1200px;height:1600px;background:var(--mist)}
.card{background:var(--paper)}
.photo{display:block}
.card-title{font-size:22px;font-weight:600;letter-spacing:.3px;text-transform:uppercase}
.card-sub{font-size:16px;font-weight:500;text-transform:uppercase;line-height:1.35;color:var(--ink)}
.card-date{font-size:13px;color:var(--muted);letter-spacing:.5px}
.card-text{font-size:11.5px;color:var(--body);line-height:1.65}
.notch{width:0;height:0;border-left:11px solid transparent;border-right:11px solid transparent;border-bottom:11px solid var(--paper)}

/* lower */
.lower{left:0;top:2267px;width:1200px;height:1046px;background:var(--fog)}
.tag{background:var(--green);color:#fff;font-size:13px;padding:4px 14px}
.overlay-title{color:#fff;font-weight:600;text-transform:uppercase}
.meta{display:flex;gap:20px;font-size:11px;color:#ddd;align-items:center}
.meta span{display:flex;align-items:center;gap:6px}
.ico{width:10px;height:10px;border:1.5px solid currentColor;display:inline-block}
.ico.round{border-radius:50%}
.section-head{font-size:22px;font-weight:600;color:var(--plum);text-transform:uppercase;letter-spacing:.5px}
.rule{height:1px;background:#d6d6d6}
.video-title{font-size:13px;font-weight:600;text-transform:uppercase;line-height:1.4;color:var(--ink)}
.video-meta{color:#666}
.play{width:54px;height:54px;border-radius:50%;border:3px solid rgba(255,255,255,.8);background:rgba(255,255,255,.2)}

/* footer */
.site-footer{left:0;top:3313px;width:1200px;height:77px;background:var(--footer);color:#fff}
.copyright{left:100px;top:30px;font-size:11px;letter-spacing:.5px}
.connect{right:100px;top:21px;display:flex;align-items:center;gap:14px;font-size:14px}
.social{width:32px;height:32px;border-radius:50%;border:1.5px solid rgba(255,255,255,.6)}
</style>
</head>
<body>

<header class="site-header abs">
  <div class="brand abs"><span class="brand-mark"></span><span class="brand-name">GARNET LOWELL<br>PTY LTD</span></div>
  <nav class="main-nav abs"><span class="active">HOME</span><span>ABOUT US</span><span>PAGES</span><span>BLOG</span><span>GALLERY</span><span>CONTACTS</span></nav>
</header>

<section class="hero abs" role="img" aria-label="Silhouette of a climber helping another up a rock at sunset">
  <h1 class="hero-title abs">WE ARE A LEADERSHIP &amp; TEAM COACHING COMPANY</h1>
  <p class="hero-sub abs">I’ve been writing short articles to support my business.</p>
  <svg class="hero-arrow abs" style="left:26px" viewBox="0 0 46 46"><path d="M27 14 L18 23 L27 32" stroke="#333" stroke-width="3" fill="none"/></svg>
  <svg class="hero-arrow abs" style="right:26px" viewBox="0 0 46 46"><path d="M19 14 L28 23 L19 32" stroke="#333" stroke-width="3" fill="none"/></svg>
</section>

<section class="articles abs">
  <article class="card abs" style="left:100px;top:30px;width:1000px;height:331px">
    <div class="photo abs" role="img" aria-label="Smiling businessman in a suit talking on a phone" style="left:0;top:0;width:745px;height:331px;background:linear-gradient(90deg,#a9a29a,#cfcac4 50%,#e6e4e2)"></div>
    <svg class="abs" style="left:645px;top:0" width="100" height="331"><polygon points="100,0 100,331 40,331" fill="#fff"/></svg>
    <h2 class="card-title abs" style="left:774px;top:28px;color:var(--teal)">Minim Veniam</h2>
    <p class="card-sub abs" style="left:774px;top:92px;width:200px">Duis aute irure dolor in reprehenderit in voluptate</p>
    <p class="card-date abs" style="left:774px;top:152px">Oct 16, 2015</p>
    <p class="card-text abs" style="left:774px;top:210px;width:210px">Fusce euismod consequat ante. Lorem ipsum dolor sit amet, consectetuer adipiscing elit. Pellentesque sed dolor. Aliquam congue fermentum nisl.</p>
  </article>

  <!-- row one -->
  <article class="card abs" style="left:100px;top:388px;width:316px;height:568px">
    <div class="photo" role="img" aria-label="Hands signing a document at a desk" style="height:251px;background:linear-gradient(135deg,#d8d8d6,#b8b4ae)"></div>
    <div class="notch abs" style="left:24px;top:240px"></div>
    <h2 class="card-title abs" style="left:18px;top:278px;color:#8a3d9c">Exercitation Ullam</h2>
    <p class="card-sub abs" style="left:18px;top:338px;width:270px">Duis aute irure dolor in reprehenderit in voluptate</p>
    <p class="card-date abs" style="left:18px;top:398px">Mar 16, 2015</p>
    <p class="card-text abs" style="left:18px;top:450px;width:270px">At vero eos et accusamus et iusto odio dignissimos ducimus qui blanditiis praesentium voluptatum deleniti atque corrupti quos dolores.</p>
  </article>
  <article class="card abs" style="left:442px;top:388px;width:316px;height:568px">
    <div class="photo" role="img" aria-label="Two businessmen shaking hands" style="height:251px;background:linear-gradient(135deg,#c9d6e2,#8fa5bc)"></div>
    <div class="notch abs" style="left:24px;top:240px"></div>
    <h2 class="card-title abs" style="left:18px;top:278px;color:var(--orchid)">Fugiat Nulla</h2>
    <p class="card-sub abs" style="left:18px;top:338px;width:260px">Voluptate velit esse cillum dolore eu</p>
    <p class="card-date abs" style="left:18px;top:398px">Apr 12, 2015</p>
    <p class="card-text abs" style="left:18px;top:450px;width:270px">Similique sunt in culpa qui officia deserunt mollitia animi, id est laborum et dolorum fuga. Et harum quidem rerum facilis est et expedita distinctio.</p>
  </article>
  <article class="card abs" style="left:784px;top:388px;width:316px;height:568px">
    <div class="photo" role="img" aria-label="Hand touching a glowing financial chart screen" style="height:251px;background:linear-gradient(135deg,#3a5e8c,#9ab8d8)"></div>
    <div class="notch abs" style="left:24px;top:240px"></div>
    <h2 class="card-title abs" style="left:18px;top:278px;color:var(--violet)">Occaecat Cupidat</h2>
    <p class="card-sub abs" style="left:18px;top:338px;width:240px">Tempora incidunt ut labore et dolor</p>
    <p class="card-date abs" style="left:18px;top:398px">May 23, 2015</p>
    <p class="card-text abs" style="left:18px;top:450px;width:270px">Nam libero tempore, cum soluta nobis est eligendi optio cumque nihil impedit quo minus id quod maxime placeat facere.</p>
  </article>

  <!-- row two -->
  <article class="card abs" style="left:100px;top:985px;width:316px;height:568px">
    <div class="photo" role="img" aria-label="Businessman smiling in an office with colleagues" style="height:251px;background:linear-gradient(135deg,#e6ecef,#8d9aa6)"></div>
    <div class="notch abs" style="left:24px;top:240px"></div>
    <h2 class="card-title abs" style="left:18px;top:278px;color:var(--blue)">Ullamco Laboris</h2>
    <p class="card-sub abs" style="left:18px;top:338px;width:280px">Fusce euismod consequat ante rem ipsum dolor sit</p>
    <p class="card-date abs" style="left:18px;top:398px">Mar 12, 2015</p>
    <p class="card-text abs" style="left:18px;top:450px;width:270px">At vero eos et accusamus et iusto odio dignissimos ducimus qui blanditiis praesentium voluptatum deleniti atque corrupti quos dolores.</p>
  </article>
  <article class="card abs" style="left:442px;top:985px;width:316px;height:568px">
    <div class="photo" role="img" aria-label="Man with raised arms on a chair facing a city skyline" style="height:251px;background:linear-gradient(180deg,#cfcfcf,#6e6e6e)"></div>
    <div class="notch abs" style="left:24px;top:240px"></div>
    <h2 class="card-title abs" style="left:18px;top:278px;color:var(--blue-deep)">Commodo Conse</h2>
    <p class="card-sub abs" style="left:18px;top:338px;width:270px">Ut enim ad minima veniam, quis nostrum</p>
    <p class="card-date abs" style="left:18px;top:398px">June 12, 2015</p>
    <p class="card-text abs" style="left:18px;top:450px;width:270px">Et harum quidem rerum facilis est et expedita distinctio. Nam libero tempore, cum soluta nobis est eligendi optio.</p>
  </article>
  <article class="card abs" style="left:784px;top:985px;width:316px;height:568px">
    <div class="photo" role="img" aria-label="Business team meeting around a laptop" style="height:251px;background:linear-gradient(135deg,#5a4036,#b89a88)"></div>
    <div class="notch abs" style="left:24px;top:240px"></div>
    <h2 class="card-title abs" style="left:18px;top:278px;color:var(--violet)">Duis Aute</h2>
    <p class="card-sub abs" style="left:18px;top:338px;width:260px">Numquam eius modi tempora incidunt ut labore</p>
    <p class="card-date abs" style="left:18px;top:398px">Feb 14, 2015</p>
    <p class="card-text abs" style="left:18px;top:450px;width:270px">Aut rerum necessitatibus saepe eveniet ut et voluptates repudiandae sint et molestiae non recusandae. Itaque earum rerum.</p>
  </article>
</section>

<section class="lower abs">
  <!-- featured news -->
  <article class="abs" role="img" aria-label="Silhouettes of a board meeting around a table before a world map" style="left:100px;top:36px;width:551px;height:297px;background:linear-gradient(180deg,#1c3a6a,#0e1d36 70%,#0a1222)">
    <span class="tag abs" style="left:228px;top:38px">Business News</span>
    <h3 class="overlay-title abs" style="left:0;width:551px;top:84px;text-align:center;font-size:18px">Mollis Quam Sollicitudin Adipiscing</h3>
    <div class="meta abs" style="left:175px;top:118px"><span><i class="ico"></i>Tom Hadley</span><span><i class="ico round"></i>04 Dec 2015</span></div>
  </article>

  <!-- small tiles -->
  <article class="abs" role="img" aria-label="Hiker on a rocky ridge" style="left:100px;top:361px;width:262px;height:188px;background:linear-gradient(180deg,#5f7894,#3a3428)">
    <h4 class="overlay-title abs" style="left:18px;top:112px;width:220px;font-size:11px;text-transform:none">Quam Mollis Venenatis Elit Lorem</h4>
    <div class="meta abs" style="left:18px;top:150px;font-size:10px"><span><i class="ico"></i>Tom Hadley</span><span><i class="ico round"></i>04 Dec 2015</span></div>
  </article>
  <article class="abs" role="img" aria-label="Cyclist riding up a mountain road" style="left:389px;top:361px;width:262px;height:188px;background:linear-gradient(180deg,#2c3c58,#1c2430)">
    <h4 class="overlay-title abs" style="left:18px;top:112px;width:220px;font-size:11px;text-transform:none">Quam Mollis Venenatis Elit Lorem</h4>
    <div class="meta abs" style="left:18px;top:150px;font-size:10px"><span><i class="ico"></i>Tom Hadley</span><span><i class="ico round"></i>04 Dec 2015</span></div>
  </article>
  <article class="abs" role="img" aria-label="Climber on an overhanging rock face" style="left:100px;top:583px;width:262px;height:188px;background:linear-gradient(135deg,#8a5a34,#3a2618)">
    <h4 class="overlay-title abs" style="left:18px;top:100px;width:130px;font-size:11px;text-transform:none">Quam Mollis Venenatis Elit Lorem</h4>
    <div class="meta abs" style="left:18px;top:150px;font-size:10px"><span><i class="ico"></i>Tom Hadley</span><span><i class="ico round"></i>04 Dec 2015</span></div>
  </article>
  <article class="abs" role="img" aria-label="Mountain biker on a forest trail" style="left:389px;top:583px;width:262px;height:188px;background:linear-gradient(135deg,#4a6a2a,#1e2e14)">
    <h4 class="overlay-title abs" style="left:18px;top:100px;width:130px;font-size:11px;text-transform:none">Quam Mollis Venenatis Elit Lorem</h4>
    <div class="meta abs" style="left:18px;top:150px;font-size:10px"><span><i class="ico"></i>Tom Hadley</span><span><i class="ico round"></i>04 Dec 2015</span></div>
  </article>
  <article class="abs" role="img" aria-label="Smiling colleagues in an office" style="left:100px;top:804px;width:262px;height:188px;background:linear-gradient(135deg,#8aa2b4,#4a5e70)">
    <h4 class="overlay-title abs" style="left:18px;top:100px;width:130px;font-size:11px;text-transform:none">Quam Mollis Venenatis Elit Lorem</h4>
    <div class="meta abs" style="left:18px;top:150px;font-size:10px"><span><i class="ico"></i>Tom Hadley</span><span><i class="ico round"></i>04 Dec 2015</span></div>
  </article>
  <article class="abs" role="img" aria-label="Hikers on a hilltop at sunset" style="left:389px;top:804px;width:262px;height:188px;background:linear-gradient(180deg,#c0482a,#5a2418 60%,#1e1410)">
    <h4 class="overlay-title abs" style="left:18px;top:100px;width:130px;font-size:11px;text-transform:none">Quam Mollis Venenatis Elit Lorem</h4>
    <div class="meta abs" style="left:18px;top:150px;font-size:10px"><span><i class="ico"></i>Tom Hadley</span><span><i class="ico round"></i>04 Dec 2015</span></div>
  </article>

  <!-- video posts -->
  <h2 class="section-head abs" style="left:714px;top:28px">Video Posts</h2>
  <div class="rule abs" style="left:714px;top:70px;width:386px"></div>

  <article class="abs" style="left:714px;top:93px;width:386px">
    <div class="photo" role="img" aria-label="Person working on a laptop on a beach chair by the sea" style="height:216px;background:linear-gradient(180deg,#4a8ad0,#b8d4ea 60%,#d8c8a8)"></div>
    <span class="play abs" style="left:166px;top:81px"></span>
    <h3 class="video-title" style="margin-top:12px">Condimentum sit inceptos fringilla lorem</h3>
    <div class="meta video-meta" style="margin-top:8px"><span><i class="ico"></i>Tom Hadley</span><span><i class="ico round"></i>04 Dec 2015</span></div>
  </article>
  <article class="abs" style="left:714px;top:395px;width:386px">
    <div class="photo" role="img" aria-label="Climber silhouetted on a cliff against a sunset sky" style="height:216px;background:linear-gradient(180deg,#7a8aa0,#d8a858 55%,#3a2a18)"></div>
    <span class="play abs" style="left:166px;top:81px"></span>
    <h3 class="video-title" style="margin-top:12px">Parturient fringilla vehicula fermentum ullamcorper</h3>
    <div class="meta video-meta" style="margin-top:8px"><span><i class="ico"></i>Nora Pell</span><span><i class="ico round"></i>04 Dec 2015</span></div>
  </article>
  <article class="abs" style="left:714px;top:718px;width:386px">
    <div class="photo" role="img" aria-label="Businessman looking out of a large office window" style="height:216px;background:linear-gradient(135deg,#3a4a68,#8a98b0 60%,#2a3040)"></div>
    <span class="play abs" style="left:166px;top:81px"></span>
    <h3 class="video-title" style="margin-top:12px">Mollis parturient vulputate vehicula</h3>
    <div class="meta video-meta" style="margin-top:8px"><span><i class="ico"></i>Nora Pell</span><span><i class="ico round"></i>04 Dec 2015</span></div>
  </article>
</section>

<footer class="site-footer abs">
  <p class="copyright abs">COPYRIGHTS © 2016 GARNET LOWELL PTY. ALL RIGHTS RESERVED.</p>
  <div class="connect abs"><span>Connect Us On:</span><span class="social"></span><span class="social"></span><span class="social"></span></div>
</footer>

</body>
</html>
```